Velantor corporate website

Dear graphic designers,
We would like to create a brand new corporate website for our company named "Velantor".
Velantor is a small Swiss premium IT company, with very prestigious clients in the Private Banking industry.
Here would be the values which could be associated to Velantor: trustworthy, serious, modern, high tech, high quality, sobriety, elegant.
Please find attached the Velantor logo in SVG format.
Our new website will have for only purpose to present briefly the company in one page: the team of experts (4 employees), the mission, the expertise and the contact info.
Very short and concise, easy to read.
Like this website for example but even shorter: https://www.mirdalex.example/

```html
<!DOCTYPE html>
<html lang="en">
<head>
<meta charset="utf-8">
<title>Velantor</title>
<link href="https://fonts.googleapis.com/css2?family=Poppins:ital,wght@0,300;0,400;0,500;0,600;1,300;1,400&display=swap" rel="stylesheet">
<style>
:root{
  --blue:#1763b8;
  --blue-dark:#0f4f9c;
  --blue-deep:#0d3f82;
  --blue-soft:#7aa9da;
  --panel:#f0f4fb;
  --ink:#1b1b1b;
  --grey:#555;
  --footer:#121212;
  --star:#f5b400;
}
*{box-sizing:border-box;margin:0;padding:0}
html,body{width:1200px;height:4286px;overflow:hidden}
body{position:relative;font-family:"Poppins",sans-serif;color:var(--ink);background:#fff}
.abs{position:absolute}
a{color:inherit;text-decoration:none}
.btn{position:absolute;height:42px;border-radius:21px;background:var(--blue-dark);color:#fff;font-size:13px;font-weight:500;letter-spacing:.3px;display:flex;align-items:center;justify-content:space-between;padding:0 10px 0 22px}
.btn .dot{width:16px;height:16px;border-radius:50%;background:#fff;position:relative}
.btn .dot::after{content:"";position:absolute;left:5px;top:4px;border-left:6px solid var(--blue-dark);border-top:4px solid transparent;border-bottom:4px solid transparent}
.brand{font-weight:500;color:var(--blue);letter-spacing:1px}

/* nav */
.nav{position:absolute;left:0;top:0;width:1200px;height:70px;background:#fff}
.nav .brand{position:absolute;left:87px;top:12px;font-size:34px}
.nav ul{list-style:none}
.nav li{position:absolute;top:28px;font-size:14px;color:#333}
.nav li.active{color:var(--blue)}
.nav li.active::after{content:"";position:absolute;left:0;top:38px;width:40px;height:3px;background:var(--blue)}

/* hero */
.hero{position:absolute;left:0;top:70px;width:1200px;height:716px;background:linear-gradient(180deg,#f6f6f4 0%,#e9e7e2 45%,#c9c6bf 70%,#8a8780 100%);clip-path:polygon(0 0,100% 0,100% 90%,0 100%)}
.hero-welcome{position:absolute;top:150px;width:1200px;text-align:center;font-size:22px;letter-spacing:2px;color:#333}
.hero-brand{position:absolute;top:176px;width:1200px;text-align:center;font-size:62px}

/* about */
.about-bg{position:absolute;left:0;top:715px;width:1200px;height:641px;background:var(--panel)}
.sec-title{font-size:37px;font-weight:600;color:var(--ink)}
.sec-title span{color:var(--blue)}
.rule{position:absolute;height:4px;width:52px;background:var(--blue)}
.body-text{font-size:15px;line-height:25px;color:#333}

/* team */
.card{position:absolute;top:1534px;width:223px;height:333px;background:#fff;box-shadow:0 4px 14px rgba(0,0,0,.12);border-radius:6px}
.card .photo{position:absolute;left:10px;top:0;width:203px;height:205px;border-radius:6px;background:linear-gradient(180deg,#efefef,#d7d7d7)}
.card .name{position:absolute;left:18px;top:226px;font-size:15px;font-weight:500}
.card .mail{position:absolute;left:18px;top:251px;font-size:10.5px;color:#555}
.card .line{position:absolute;left:18px;top:281px;width:26px;height:1px;background:#999}
.card .role{position:absolute;left:18px;top:297px;font-size:11.5px;font-weight:500}
.card .in{position:absolute;right:18px;top:232px;width:18px;height:18px;border-radius:3px;background:var(--blue)}

/* mission & expertise */
.mission-photo{position:absolute;left:0;top:2034px;width:594px;height:502px;background:linear-gradient(135deg,#5a6e85 0%,#b9c2cc 45%,#8a97a8 75%,#3d4c60 100%)}
.mission-tab{position:absolute;left:283px;top:2335px;width:311px;height:201px;background:rgba(23,99,184,.88);border-top-left-radius:170px}
.expertise{position:absolute;left:604px;top:2034px;width:596px;height:502px;background:var(--blue)}
.band-title{position:absolute;color:#fff;font-size:29px;font-weight:500}
.band-link{position:absolute;color:#fff;font-size:14px;text-decoration:underline}
.arrow{position:absolute;height:1px;background:#fff}
.arrow::after{content:"";position:absolute;right:0;top:-4px;width:8px;height:8px;border-right:1px solid #fff;border-top:1px solid #fff;transform:rotate(45deg)}

/* testimonials */
.t-card{position:absolute;top:2704px;height:366px;background:#fff;box-shadow:0 4px 18px rgba(0,0,0,.12);border-radius:6px}
.t-card.side{opacity:.5}
.t-quote{font-style:italic;font-weight:300;font-size:15px;line-height:25px;text-align:center;color:#333}
.qmark{position:absolute;font-size:90px;font-weight:600;line-height:1;color:#222;font-family:Georgia,serif}
.t-arrow{position:absolute;width:66px;height:66px;border-radius:50%;background:var(--blue)}

/* contact */
.form-panel{position:absolute;left:652px;top:3183px;width:438px;height:591px;background:var(--blue-soft)}
.field{position:absolute;left:40px;width:361px;height:42px;background:var(--blue);color:#e6eefa;font-size:12px;padding:12px 18px}
.c-icon{position:absolute;left:110px;width:52px;height:52px;border-radius:50%;background:#fff}
.c-label{position:absolute;left:185px;font-size:18px;color:#d5e3f5;font-weight:300}
.c-value{position:absolute;left:185px;font-size:20px;color:#fff;line-height:29px}

/* footer */
.footer{position:absolute;left:0;top:3861px;width:1200px;height:425px;background:var(--footer);color:#fff}
.f-col{position:absolute;top:0;height:300px;border-left:1px solid #3a3a3a}
.f-col h4{position:absolute;left:20px;top:86px;font-size:17px;font-weight:600;white-space:nowrap}
.f-col h4::after{content:"";position:absolute;left:0;top:34px;width:50px;height:2px;background:var(--blue)}
.f-col h4::before{content:"";position:absolute;left:-21px;top:0;width:3px;height:24px;background:var(--blue)}
.f-col ul{position:absolute;left:22px;top:148px;list-style:none;font-size:12.5px;line-height:26px;white-space:nowrap}
</style>
</head>
<body>

<header class="nav">
  <div class="brand">Velantor</div>
  <ul>
    <li class="active" style="left:371px">Home</li>
    <li style="left:451px">About Us</li>
    <li style="left:551px">Services</li>
    <li style="left:651px">Team</li>
    <li style="left:734px">The Mission</li>
    <li style="left:855px">The Expertise</li>
  </ul>
  <a class="btn" style="left:978px;top:17px;width:147px;height:40px;font-size:13px;padding-left:20px">CONTACT US <span class="dot"></span></a>
</header>

<section>
  <div class="hero" role="img" aria-label="Photo of three colleagues working together at a table in a bright office"></div>
  <div class="hero-welcome" style="top:150px">WELCOME TO</div>
  <div class="hero-brand brand">Velantor</div>
  <a class="btn" style="left:526px;top:284px;width:146px">GET STARTED <span class="dot"></span></a>
  <div class="abs" style="left:575px;top:672px;width:7px;height:7px;border-radius:50%;background:#ddd"></div>
  <div class="abs" style="left:588px;top:672px;width:7px;height:7px;border-radius:50%;background:var(--blue)"></div>
  <div class="abs" style="left:599px;top:676px;width:2px;height:134px;background:var(--blue)"></div>
</section>

<section>
  <div class="about-bg"></div>
  <div class="abs" style="left:110px;top:894px;width:466px;height:382px;display:flex;align-items:center;justify-content:center;gap:20px">
    <div style="width:56px;height:56px;border-radius:50%;background:var(--blue-soft)"></div>
    <div class="brand" style="font-size:64px">Velantor</div>
  </div>
  <h2 class="sec-title abs" style="left:619px;top:890px">About <span>Us</span></h2>
  <div class="rule" style="left:619px;top:950px"></div>
  <p class="body-text abs" style="left:616px;top:974px;width:476px">Saerspiciatis undeaseopoiise osamnis istasesee njhhjkatus error sit voluptatem accusan tium doloreasmque laudantium, totam rem aperiam, ease aque ipaefdsa quae ab illo inventore veritatis ease quasi architecto beatae vitae diascta sunt explicabo. Nemo enim ipsam voluptatem quia volupta sde sessitasese aspernatur autodit aut fugitsdsed quia conseq aauuntur magni dolores eos qui ratione voluptatem sequi nesciunt.</p>
  <a class="btn" style="left:616px;top:1195px;width:146px">LEARN MORE <span class="dot"></span></a>
</section>

<section>
  <h2 class="sec-title abs" style="left:0;width:1200px;text-align:center;top:1418px">Our <span>Team</span></h2>
  <div class="rule" style="left:574px;top:1472px"></div>

  <div class="card" style="left:111px"><div class="photo" role="img" aria-label="Portrait of team member"></div><div class="name">Daniel Morrow</div><div class="mail">daniel.morrow@mail.example</div><div class="line"></div><div class="role">Founder and Senior Consultant</div><div class="in"></div></div>
  <div class="card" style="left:363px"><div class="photo" role="img" aria-label="Portrait of team member"></div><div class="name">Daniel Morrow</div><div class="mail">daniel.morrow@mail.example</div><div class="line"></div><div class="role">Founder and Senior Consultant</div><div class="in"></div></div>
  <div class="card" style="left:614px"><div class="photo" role="img" aria-label="Portrait of team member"></div><div class="name">Daniel Morrow</div><div class="mail">daniel.morrow@mail.example</div><div class="line"></div><div class="role">Founder and Senior Consultant</div><div class="in"></div></div>
  <div class="card" style="left:865px"><div class="photo" role="img" aria-label="Portrait of team member"></div><div class="name">Daniel Morrow</div><div class="mail">daniel.morrow@mail.example</div><div class="line"></div><div class="role">Founder and Senior Consultant</div><div class="in"></div></div>

  <a class="btn" style="left:526px;top:1905px;width:146px">VIEW ALL <span class="dot"></span></a>
</section>

<section>
  <div class="mission-photo" role="img" aria-label="Photo of colleagues reviewing a tablet in a warehouse"></div>
  <div class="mission-tab"></div>
  <h3 class="band-title" style="left:363px;top:2424px">THE MISSION</h3>
  <a class="band-link" style="left:363px;top:2470px">Learn More</a>
  <div class="arrow" style="left:461px;top:2483px;width:85px"></div>

  <div class="expertise" role="img" aria-label="Blue-tinted photo of a team meeting"></div>
  <h3 class="band-title" style="left:604px;width:596px;text-align:center;top:2110px">THE EXPERTISE</h3>
  <p class="body-text abs" style="left:677px;top:2193px;width:413px;color:#fff;text-align:justify;text-align-last:center">Saerspiciatis undease saeoiispoiise osamnis istasesee njhhjkatus error s;lsaepit voluptatem accusan tium doloreasmque laudantium, totam rem aperiam, ease aque ipaefdsa quae ab illo inventore veritatis ease quasi architecto beatae vitae diascta sunt explicabo. Nemo enim ipsam voluptatem quia volupta sde sessitasese aspernatur autodit alksdjoseut fugitsdsed quia conseq aauuntur magni dolores eosaels qui ratione voluptatem sequi nesciunt.</p>
  <a class="band-link" style="left:809px;top:2480px">Learn More</a>
  <div class="arrow" style="left:907px;top:2493px;width:86px"></div>
</section>

<section>
  <h2 class="sec-title abs" style="left:0;width:1200px;text-align:center;top:2604px;font-size:39px">Testimonials</h2>
  <div class="rule" style="left:574px;top:2660px"></div>

  <div class="t-card side" style="left:-330px;width:601px">
    <p class="t-quote abs" style="left:40px;top:72px;width:520px">Saerspiciatis undeasepoiise osamnis istasesee njhhjkatus error sit voluptatem accusan tium doloreasmque laudantium, totam rem aperiam, ease aque ipaefdsa quae ab illo inventore veritatis ease quasi architecto beatae vitae diascta sunt explicabo. Nemo enim ipsam voluptatem quia volupta sde sessitasese aspernatur autodit aut fugitsdsed quia conseq.</p>
    <div class="qmark" style="left:530px;top:228px">&rdquo;</div>
  </div>
  <div class="t-card side" style="left:927px;width:601px">
    <div class="qmark" style="left:20px;top:30px">&ldquo;</div>
    <p class="t-quote abs" style="left:68px;top:72px;width:520px">Saerspiciatis undeasepoiise osamnis istasesee njhhjkatus error sit voluptatem accusan tium doloreasmque laudantium, totam rem aperiam, ease aque ipaefdsa quae ab illo inventore veritatis ease quasi architecto beatae vitae diascta sunt explicabo. Nemo enim ipsam voluptatem quia volupta sde sessitasese aspernatur autodit aut fugitsdsed quia conseq.</p>
  </div>

  <div class="t-card" style="left:296px;width:606px">
    <div class="qmark" style="left:22px;top:30px">&ldquo;</div>
    <p class="t-quote abs" style="left:66px;top:66px;width:476px">Saerspiciatis undeasepoiise osamnis istasesee njhhjkatus error sit voluptatem accusan tium doloreasmque laudantium, totam rem aperiam, ease aque ipaefdsa quae ab illo inventore veritatis ease quasi architecto beatae vitae diascta sunt explicabo. Nemo enim ipsam voluptatem quia volupta sde sessitasese aspernatur autodit aut fugitsdsed quia conseq.</p>
    <div class="qmark" style="left:542px;top:222px">&rdquo;</div>
    <div class="abs" style="left:0;width:606px;top:253px;text-align:center;color:var(--star);font-size:24px;letter-spacing:1px">&#9733;&#9733;&#9733;&#9733;&#9733;</div>
    <div class="abs" style="left:0;width:606px;top:304px;text-align:center;font-size:16px;font-weight:500">Daniel Morrow</div>
    <div class="abs" style="left:0;width:606px;top:328px;text-align:center;font-size:11px;color:#555">Consultant</div>
  </div>

  <div class="t-arrow" style="left:110px;top:2854px">
    <svg width="66" height="66" viewBox="0 0 66 66"><path d="M42 33H24M31 25l-8 8 8 8" fill="none" stroke="#fff" stroke-width="2.5" stroke-linecap="round" stroke-linejoin="round"/></svg>
  </div>
  <div class="t-arrow" style="left:1019px;top:2854px">
    <svg width="66" height="66" viewBox="0 0 66 66"><path d="M24 33h18M35 25l8 8-8 8" fill="none" stroke="#fff" stroke-width="2.5" stroke-linecap="round" stroke-linejoin="round"/></svg>
  </div>
</section>

<section>
  <svg class="abs" style="left:0;top:3183px" width="1200" height="678" viewBox="0 0 1200 678">
    <polygon points="0,0 640,0 652,30 1200,110 1200,678 0,678" fill="#1f5fb0"/>
    <polygon points="0,0 640,0 652,30 0,30" fill="#2a6bbb"/>
  </svg>
  <div class="abs" role="img" aria-label="Blue-tinted photo of a workspace" style="left:0;top:3213px;width:652px;height:648px;background:linear-gradient(135deg,rgba(255,255,255,.04),rgba(0,0,0,.06))"></div>

  <h2 class="abs" style="left:110px;top:3346px;font-size:38px;font-weight:600;color:#fff">Contact Us</h2>
  <div class="rule" style="left:110px;top:3404px;background:#fff"></div>
  <p class="abs" style="left:110px;top:3426px;width:500px;font-size:16px;line-height:28px;color:#fff">Saerspiciatis undeasepoiise osamnis istasesee njhhjkatus error sit voluptatem accusan tium doloreasm.</p>

  <div class="c-icon" style="top:3524px"><svg width="52" height="52" viewBox="0 0 52 52"><path d="M26 14c-5 0-9 4-9 9 0 7 9 16 9 16s9-9 9-16c0-5-4-9-9-9z" fill="var(--blue)"/><circle cx="26" cy="23" r="3.5" fill="#fff"/></svg></div>
  <div class="c-label" style="top:3520px">Address</div>
  <div class="c-value" style="top:3546px">42 Linden Row, Maple Hill<br>Ontario, Canada, 10427</div>

  <div class="c-icon" style="top:3632px"><svg width="52" height="52" viewBox="0 0 52 52"><path d="M19 15l5 0 2 6-3 2c1 3 4 6 7 7l2-3 6 2v5c0 1-1 2-2 2-11-1-18-8-19-19 0-1 1-2 2-2z" fill="var(--blue)"/></svg></div>
  <div class="c-label" style="top:3633px">Call Us</div>
  <div class="c-value" style="top:3656px">+1 (555) 014-2290</div>

  <div class="c-icon" style="top:3712px"><svg width="52" height="52" viewBox="0 0 52 52"><rect x="15" y="18" width="22" height="16" rx="2" fill="var(--blue)"/><path d="M15 19l11 8 11-8" fill="none" stroke="#fff" stroke-width="1.8"/></svg></div>
  <div class="c-label" style="top:3713px">Email</div>
  <div class="c-value" style="top:3736px">info@velantor.example</div>

  <div class="form-panel">
    <h2 class="abs" style="left:37px;top:40px;font-size:38px;font-weight:600;color:#fff">Get In Touch</h2>
    <div class="abs" style="left:40px;top:92px;font-size:13px;color:#fff">OR CALL US +1 (555) 014-2290</div>
    <div class="field" style="top:135px">Your Name</div>
    <div class="field" style="top:195px">Email</div>
    <div class="field" style="top:255px">Phone Number</div>
    <div class="field" style="top:315px;height:156px">Write a message</div>
    <a class="btn" style="left:40px;top:493px;width:145px;height:40px;background:#fff;color:var(--blue)">SUBMIT <span class="dot" style="background:var(--blue)"></span></a>
  </div>
</section>

<footer class="footer">
  <div class="brand abs" style="left:110px;top:140px;font-size:58px;color:var(--blue)">Velantor</div>
  <div class="abs" style="left:242px;top:216px;width:32px;height:32px;border-radius:50%;background:#333"></div>
  <div class="abs" style="left:286px;top:216px;width:32px;height:32px;border-radius:50%;background:#333"></div>

  <div class="f-col" style="left:503px"><h4>QUICK LINKS</h4><ul><li>HOME</li><li>ABOUT US</li><li>SERVICES</li><li>TEAM</li><li>THE MISSION</li><li>THE EXPERTISE</li></ul></div>
  <div class="f-col" style="left:754px"><h4>LINKS</h4><ul><li>COPYRIGHT</li><li>LEGAL</li><li>PRIVACY</li><li>ACCESSIBILITY</li><li>SITEMAP</li></ul></div>
  <div class="f-col" style="left:962px"><h4>SUPPORT</h4><ul><li>TEAM</li><li>ABOUT US</li><li>CAREERS</li><li>OUR VALUES</li><li>CONTACT US</li></ul></div>

  <div class="abs" style="left:1115px;top:334px;width:38px;height:38px;border-radius:5px;background:var(--blue)">
    <svg width="38" height="38" viewBox="0 0 38 38"><path d="M14 22l5-5 5 5" fill="none" stroke="#fff" stroke-width="2" stroke-linecap="round"/></svg>
  </div>
  <div class="abs" style="left:0;width:1200px;top:378px;text-align:center;font-size:14px;color:#ddd">©2023. All rights reserved.</div>
</footer>

</body>
</html>
```